Broschüre für Konzepte rund um Immobilien
Zielgruppe
Wir sind ein junges, dynamisches Team und unterstützen Kunden mit individuellen, abgestimmten Konzepten rund um Ihre Immobilie - daher suchen wir ein hochwertiges Design, unsere Zielgruppe liegt Wert auf was neues, nicht das was jeder hat.
Aufgabenstellung
Die Farben und das Layout sollen von der Homepage übernommen werden www.zq-plan.de..
Den Text entnehmen Sie der angehängten Datei. Bilder, Anordnungen und sonstiges überlasse ich Ihren kreativen Geist! DIN A5 Querformat - Bilder und Texte müssen in einer sehr hohen Auflösung umsetzbar sein!

```html
<!DOCTYPE html>
<html lang="de">
<head>
<meta charset="utf-8">
<title>ZQPLAN Broschüre – Umschlag</title>
<link rel="stylesheet" href="https://fonts.googleapis.com/css2?family=Open+Sans:wght@400;600;700&display=swap">
<style>
  :root {
    --navy: #1a202d;
    --white: #ffffff;
    --canvas: #ebebec;
    --logo-grey: #8a8d93;
    --text-light: #e6e8ec;
    --photo-warm: #9a7a5e;
    --photo-light: #e9ebe8;
    --photo-dark: #3b3c3f;
  }
  * { margin: 0; padding: 0; box-sizing: border-box; }
  html, body { width: 923px; height: 1200px; overflow: hidden; }
  body {
    background: var(--canvas);
    font-family: "Open Sans", Arial, sans-serif;
    position: relative;
  }
  .cover {
    position: absolute;
    left: 141px;
    width: 640px;
    height: 452px;
    background: var(--white);
    box-shadow: 6px 10px 14px rgba(0,0,0,0.35);
    overflow: hidden;
  }
  .cover--front { top: 70px; }
  .cover--back { top: 650px; }

  .cover__photo {
    position: absolute; left: 0; top: 0; width: 100%; height: 250px;
    background: linear-gradient(100deg, var(--photo-dark) 0%, var(--photo-light) 28%, var(--photo-warm) 48%, var(--photo-light) 70%, var(--photo-dark) 100%);
  }
  .cover__band {
    position: absolute; left: 0; width: 100%; background: var(--navy);
  }
  .cover--front .cover__band { top: 250px; height: 146px; }
  .cover--front .cover__slant { position: absolute; left: 0; top: 236px; width: 100%; height: 24px; }

  .cover--back .cover__band--top { top: 0; height: 234px; }
  .cover--back .cover__band--main { top: 242px; height: 178px; }

  .brand {
    position: absolute; display: flex; flex-direction: column; align-items: center;
    color: var(--logo-grey);
  }
  .brand__dot {
    width: 46px; height: 46px; border-radius: 50%;
    border: 5px solid var(--logo-grey); margin-bottom: 6px;
  }
  .brand__name { font-size: 24px; font-weight: 600; letter-spacing: 1px; }
  .cover--front .brand { left: 42px; top: 278px; }
  .cover--back .brand { left: 110px; top: 290px; }

  .claim { position: absolute; left: 176px; top: 303px; color: var(--white); }
  .claim__title { font-size: 16px; font-weight: 700; letter-spacing: 2.4px; }
  .claim__sub {
    font-size: 11.5px; font-weight: 400; color: var(--text-light);
    padding: 4px 0 5px; border-bottom: 1px solid var(--text-light); width: 330px;
  }

  .contact { position: absolute; left: 256px; top: 282px; color: var(--text-light); }
  .contact__head {
    font-size: 16px; font-weight: 700; color: var(--white); letter-spacing: 1px;
    padding-bottom: 10px; border-bottom: 1px solid var(--text-light); width: 264px;
  }
  .contact__head span { font-size: 11.5px; letter-spacing: 0.5px; }
  .contact__line { font-size: 12.5px; line-height: 17px; }
  .contact__line:first-of-type { margin-top: 10px; }
  .contact__web { font-size: 12.5px; font-weight: 700; color: var(--white); margin-top: 12px; }
</style>
</head>
<body>
  <section class="cover cover--front">
    <div class="cover__photo" role="img" aria-label="Foto eines hellen Wohnzimmers mit braunem Ledersofa, gemusterten Kissen und großen Fenstern"></div>
    <div class="cover__band"></div>
    <svg class="cover__slant" viewBox="0 0 640 24" preserveAspectRatio="none" aria-hidden="true">
      <polygon points="0,14 640,0 640,14 0,24" fill="var(--navy)"/>
      <polygon points="0,10 640,2 640,6 0,14" fill="var(--white)"/>
    </svg>
    <div class="brand">
      <div class="brand__dot"></div>
      <div class="brand__name">ZQPLAN</div>
    </div>
    <div class="claim">
      <div class="claim__title">BERATEN • BETREUEN • BEGLEITEN</div>
      <div class="claim__sub">Kompetenz und Know-How im Wohnungsbau</div>
    </div>
  </section>

  <section class="cover cover--back">
    <div class="cover__band cover__band--top"></div>
    <div class="cover__band cover__band--main"></div>
    <div class="brand">
      <div class="brand__dot"></div>
      <div class="brand__name">ZQPLAN</div>
    </div>
    <div class="contact">
      <div class="contact__head">ZQPLAN - <span>Peltgrubner</span></div>
      <div class="contact__line">Lindenhofer Gasse 4 | 54321 Talbrück</div>
      <div class="contact__line">T: 01234-5678901 | E: info@zq-plan.de</div>
      <div class="contact__web">www.zq-plan.de</div>
    </div>
  </section>
</body>
</html>
```